Learn to play polo (that's on horses) business, requires a roadside sign.

We need a signage design for a company based on the edge of Sydney called 'Brenta Mallet'. We sell and manage all things polo. We agist horses, breed, train sell polo ponies, provide polo lessons and manage polo ponies for clients. We also sell polo equipment.
We are trying to attract more people to have a go at learning to play polo as we want to build this side of the business. The business owner and polo coach is a previous World Cup captain and professional polo player. Our logo colours are black and white and the logo can be reversed to be white on black. The sign will be placed on the roadside on a direct route into the Sydney CBD. The final design should encompass social, fun, exercise, outdoor themes.
Updates

Target Market(s)

Highway traffic including;
Current horse riders or horse lovers (including children aged 12 - 18). It is not essential to have ridden before to partake in our lessons
A and AB socio-economic groups. Some live in the area and work in the CBD, some commute to CBD

Industry/Entity Type

Business

Font styles to use
Sans Serif

Requirements
Must have
• Brenta Mallet Pty Ltd
• Learn to Play Polo (or similar)
• www.brentamallet.com.au
• 0412 906 258
• Dimensions of sign - 1.5m (w) x 1m (h) Learn to play polo Brenta Mallet Pty Ltd www.brentamallet.com.au p - 02 6194 2086 m - 0412 906 258
Nice to have
• Themes of social, exercise, excitement, adrenalin.
• Is a sport that offers more. There is scope for family/friends to enjoy beautiful surrounds at the same time as lesson.
Should not have
• Crassness, image that polo lessons are only accessible to elite/ rich.

```html
<!DOCTYPE html>
<html lang="en">
<head>
<meta charset="utf-8">
<title>Brenta Mallet – Roadside Sign</title>
<link href="https://fonts.googleapis.com/css2?family=Questrial&family=Didact+Gothic&family=Gochi+Hand&display=swap" rel="stylesheet">
<style>
  :root {
    --ink: #000000;
    --paper: #ffffff;
    --frame: #050505;
    --shadow: rgba(0, 0, 0, 0.45);
    --grass: #dfe8d2;
    --tree: #5f7f4a;
    --horse: #7a4426;
  }
  * { margin: 0; padding: 0; box-sizing: border-box; }
  html, body { width: 1200px; height: 1000px; overflow: hidden; background: var(--paper); }
  .canvas { position: relative; width: 1200px; height: 1000px; background: var(--paper); }

  .sign {
    position: absolute; left: 40px; top: 218px; width: 1118px; height: 564px;
    background: var(--paper);
    border: 14px solid var(--frame);
    box-shadow: 4px 5px 6px var(--shadow);
    font-family: "Questrial", "Didact Gothic", sans-serif;
    color: var(--ink);
  }

  .brand-name {
    position: absolute; left: 20px; top: 36px;
    font-size: 44px; letter-spacing: 1px; white-space: nowrap; font-weight: 400;
  }
  .brand-url {
    position: absolute; left: 20px; top: 106px;
    font-size: 22px; font-weight: 700; letter-spacing: 2.6px;
    font-family: "Didact Gothic", sans-serif;
  }

  .services { position: absolute; left: 24px; top: 172px; list-style: none; }
  .services li { font-size: 33px; letter-spacing: 4.2px; line-height: 45px; }

  .contact { position: absolute; right: 680px; top: 432px; text-align: right; }
  .contact-title { font-size: 24px; font-weight: 700; letter-spacing: 5px; line-height: 34px; font-family: "Didact Gothic", sans-serif; }
  .contact-line { font-size: 24px; font-weight: 700; letter-spacing: 3.4px; line-height: 35px; font-family: "Didact Gothic", sans-serif; }

  .rider-mark {
    position: absolute; left: 14px; top: 420px; width: 84px; height: 98px;
    background: var(--ink); border-radius: 40% 45% 20% 30%;
  }

  .tagline {
    position: absolute; left: 476px; top: 26px;
    font-family: "Gochi Hand", cursive; font-size: 46px; letter-spacing: 5px; white-space: nowrap;
  }

  .photo {
    position: absolute; left: 406px; top: 82px; width: 660px; height: 390px;
    background:
      radial-gradient(ellipse 40% 30% at 55% 62%, var(--horse) 0%, rgba(122,68,38,0.6) 60%, transparent 100%),
      linear-gradient(180deg, var(--tree) 0%, #7d9866 55%, var(--grass) 72%, #f2f5ec 100%);
    -webkit-mask-image: radial-gradient(ellipse 52% 55% at 50% 50%, #000 70%, transparent 100%);
    mask-image: radial-gradient(ellipse 52% 55% at 50% 50%, #000 70%, transparent 100%);
  }

  .headline {
    position: absolute; left: 486px; top: 448px;
    font-size: 42px; font-weight: 700; letter-spacing: 3.4px; white-space: nowrap;
    font-family: "Didact Gothic", sans-serif;
  }
  .subline {
    position: absolute; left: 487px; top: 502px;
    font-size: 24px; letter-spacing: 2.6px; white-space: nowrap;
  }
</style>
</head>
<body>
<div class="canvas">
  <section class="sign">
    <h1 class="brand-name">BRENTA MALLET</h1>
    <p class="brand-url">www.brentamallet.com.au</p>

    <ul class="services">
      <li>Lessons</li>
      <li>Training</li>
      <li>Schooling</li>
      <li>Agistment &amp;</li>
      <li>Equipment Sales.</li>
    </ul>

    <div class="rider-mark" role="img" aria-label="Silhouette of a polo player on horseback swinging a mallet"></div>

    <div class="contact">
      <p class="contact-title">Contact us now</p>
      <p class="contact-line">m: 0412 906 258</p>
      <p class="contact-line">ph: 02 6194 2086</p>
    </div>

    <p class="tagline">a sport that offers more</p>

    <div class="photo" role="img" aria-label="Photo of four polo players on horses riding towards the viewer on a grass field with trees behind"></div>

    <h2 class="headline">Learn to Play Polo</h2>
    <p class="subline">in a friendly &amp; relaxing setting</p>
  </section>
</div>
</body>
</html>
```